Business Card Design

Please visit www.RobHartwell.com to acquire information for business card.

Back Side of Card:
a lifetime of experience working for you.

With over 25 years in the construction industry, well over a decade as a licensed Subcontractor / General Contractor and nearly 10 years as a licensed Realtor, I have excelled and cultivated a working knowledge of how all the pieces fit together.

Here is a link to folder.
https://files.examplestore.net/folderview?id=7Kq2XwPmR4tLvN9sBz8yHc3DfGaJ&usp=sharing

Industry/Entity Type

Construction

Contact Information for Business Card

Company: Rob Hartwell, LLC.
Address: 31872 W. Cedar Hollow Blvd. Suite 207-384
Name: Rob Hartwell
Phone: (623) 587-2914
Web: www.RobHartwell.com
Type of services offered: Architectural Design, 3D Models, Renderings & Animation - Construction Documents - Project Managment.

```html
<!DOCTYPE html>
<html lang="en">
<head>
<meta charset="utf-8">
<title>Rob Hartwell, LLC — Business Card</title>
<link href="https://fonts.googleapis.com/css2?family=Arimo:wght@400&display=swap" rel="stylesheet">
<style>
  :root {
    --page: #ffffff;
    --card-stone: #dcdbd4;
    --ink: #111111;
    --ink-soft: #1a1a1a;
    --mark-frame: #000000;
    --mark-fill: #ffffff;
    --plan-paper: #f1f1ee;
    --plan-light: #e4e4df;
    --plan-mid: #cfcfc8;
    --plan-dark: #a9a9a2;
    --plan-shadow: #8f8f89;
  }
  * { box-sizing: border-box; margin: 0; padding: 0; }
  html, body { width: 1200px; height: 1000px; overflow: hidden; background: var(--page); }
  body { position: relative; font-family: "Arimo", Arial, sans-serif; color: var(--ink); }

  .side-label { position: absolute; font-size: 45px; line-height: 1; color: var(--ink); }
  .side-label--front { left: 843px; top: 30px; }
  .side-label--back { left: 247px; top: 929px; font-size: 46px; }

  .card { position: absolute; overflow: hidden; }
  .card--front { left: 26px; top: 26px; width: 804px; height: 470px; background: var(--card-stone); }
  .card--back { left: 375px; top: 507px; width: 802px; height: 468px; }

  .brand-square {
    position: absolute; left: 42px; top: 37px; width: 194px; height: 193px;
    background: var(--mark-fill); border: 3px solid var(--mark-frame);
    outline: 1px solid var(--mark-frame); outline-offset: -7px;
    display: flex; align-items: center; justify-content: center;
    font-size: 20px; line-height: 1; color: var(--ink); text-align: center;
  }
  .company-name { position: absolute; left: 46px; top: 238px; font-size: 24px; line-height: 1; font-weight: 400; }
  .services { position: absolute; left: 46px; top: 291px; list-style: none; font-size: 17.5px; line-height: 21.3px; }

  .contact { position: absolute; right: 37px; top: 235px; text-align: right; }
  .contact__name { font-size: 51px; line-height: 56px; font-weight: 400; }
  .contact__phone { font-size: 24px; line-height: 26px; }
  .contact__address { font-size: 17px; line-height: 22px; font-style: normal; }
  .contact__web { font-size: 15px; line-height: 20px; }

  .plan-photo {
    position: absolute; inset: 0;
    background:
      radial-gradient(ellipse 70% 60% at 62% 30%, var(--plan-paper) 0%, rgba(241,241,238,0) 70%),
      linear-gradient(200deg, var(--plan-light) 0%, var(--plan-mid) 45%, var(--plan-dark) 80%, var(--plan-shadow) 100%);
  }
  .tagline { position: absolute; left: 21px; top: 30px; font-size: 24.5px; line-height: 1; color: var(--ink-soft); }
  .bio {
    position: absolute; left: 0; right: 0; top: 391px; padding: 0 10px;
    text-align: center; font-size: 16.6px; line-height: 21px; color: var(--ink);
  }
</style>
</head>
<body>
  <div class="side-label side-label--front">Front</div>
  <div class="side-label side-label--back">Back</div>

  <section class="card card--front">
    <div class="brand-square">Rob Hartwell, LLC.</div>
    <h2 class="company-name">Rob Hartwell, LLC</h2>
    <ul class="services">
      <li>Architectural Design.</li>
      <li>3D Modeling.</li>
      <li>Rendering &amp; Animation.</li>
      <li>Construction Documents.</li>
      <li>Project Management.</li>
    </ul>
    <div class="contact">
      <h1 class="contact__name">Rob Hartwell</h1>
      <div class="contact__phone">(623) 587-2914</div>
      <address class="contact__address">31872 W. Cedar Hollow Blvd<br>Suite 207-384<br>Glendale, Arizona 85310</address>
      <div class="contact__web">www.RobHartwell.com<br>info@robhartwell.com</div>
    </div>
  </section>

  <section class="card card--back">
    <div class="plan-photo" role="img" aria-label="Photograph of an architectural floor plan blueprint on paper, seen at an angle"></div>
    <p class="tagline">....a lifetime of experience working for you.</p>
    <p class="bio">With over 25 years in the construction industry, well over a decade as a licensed Subcontractor /<br>General Contractor and nearly 10 years as a licensed Realtor, I have excelled and<br>cultivated a working knowledge of how all the pieces fit together.</p>
  </section>
</body>
</html>
```